Business Card Design and Stationary design for consulting firm

Harbourline Sourcing are looking for a new business card design and a design for their A4 letterhead / A4 invoices.

We are seeking to heavily increase our brand awareness and require a business card that's professional in appearance but also shows flare and innovation. A card design that people will remember.

About Us
Harbourline Sourcing are `The Sourcing Crew’.
Our mission is to be one of Australia’s greatest companies. Our aim is to help our customers achieve the best result from their purchasing experience.

Our Requirement:
• IMPACT! IMPACT! IMPACT!
• BUSINESS & PROFESSIONAL LOOKING

• Our business colours are orange, blue and green (See the logo attached).

We have provided an Art Design specification (attached) that needs to be followed for you to win the design. This also has the font, which is used on the logo.

We are after a two sided business card

Side One should have the:
The company Logo
The Sourcing Crew
www.harbourlinesourcing.com.au
Procure | Personnel | Probity & Privacy
Sydney | Melbourne | Adelaide | Brisbane

Side Two
Logo (optional)
Harbourline Sourcing (optional)
Employee details (details listed below)

The above format is our preferred option, but if you think you can come up with something better, feel free to put it forward.

We are leaving the design up to you, but it must incorporate the logo.

We will need a template that we can change the employee details on, as we will be adding more staff over the coming months.

The details below are for one employee per card with the same design.
------------------------

Employee Details:

Marcus Del Arroyo MBA, MMgmtStratProc
Principal Consultant
0491 372 618
Marcus@harbourlinesourcing.com.au

Brianna Tolley
Consulting Manager
0462 915 308
Brianna@harbourlinesourcing.com.au

Our website is www.harbourlinesourcing.com.au

The Letterhead / invoice needs to incorporate:
the company Logo
The Sourcing Crew
Sydney | Melbourne | Adelaide | Brisbane but otherwise the design is over to you.

This file needs to be delivered in word format as other detail will be added to the documents.

We look forward to you award winning designs. If you require any further information please feel free to contact us.

Regards
Harbourline Sourcing

Target Market(s)

Our Target market is companies with 80+ employees. The market we segment is heavily male based, between the ages of 35-55 years of age.

Industry/Entity Type

Consulting

Contact Information for Business Card

See Project Description

Font styles to use
Other font styles liked:
• See Art Specification

Requirements
Must have
• Company Colours, See Project Description
Should not have
• Be outside the Art specification guidelines

```html
<!DOCTYPE html>
<html lang="en">
<head>
<meta charset="utf-8">
<title>Harbourline Sourcing — Invoice</title>
<link rel="stylesheet" href="https://fonts.googleapis.com/css2?family=Lato:wght@400;700&family=Raleway:wght@300;500&family=Cutive+Mono&display=swap">
<style>
:root{
  --blue:#3d86cc;
  --blue-light:#5cb5e8;
  --blue-deep:#2f78c2;
  --grey-cell:#e6e6e6;
  --grey-cell-alt:#ececec;
  --grey-box:#dcdcdc;
  --ink:#3a3a3a;
  --ink-soft:#8a8a8a;
  --red:#d9482b;
  --green:#4aa834;
  --orange:#ef8a2c;
  --paper:#ffffff;
  --backdrop:#eceae6;
}
*{box-sizing:border-box;margin:0;padding:0}
html,body{width:1200px;height:1180px;overflow:hidden;background:var(--backdrop)}
body{position:relative;font-family:"Lato",sans-serif;color:var(--ink)}
.sheet{position:absolute;left:197px;top:20px;width:806px;height:1140px;background:var(--paper);overflow:hidden;box-shadow:0 2px 10px rgba(0,0,0,.12)}

.brand{position:absolute;left:56px;top:120px;display:flex;align-items:center;gap:10px}
.brand-dot{width:16px;height:16px;border-radius:50%;background:var(--blue)}
.brand-name{font-family:"Lato",sans-serif;font-weight:700;font-size:22px;color:var(--ink);letter-spacing:.5px}

.contacts{position:absolute;left:470px;top:64px;list-style:none;font-family:"Cutive Mono",monospace;font-size:12px;letter-spacing:1px;color:var(--ink)}
.contacts li{display:flex;align-items:center;gap:10px;height:19px}
.contacts svg{width:12px;height:12px;flex:none}

.invoice-title{position:absolute;left:410px;top:150px;width:370px;height:56px;background:var(--blue);color:#fff;font-family:"Raleway",sans-serif;font-weight:300;font-size:38px;letter-spacing:3px;display:flex;align-items:center;justify-content:center}
.invoice-meta{position:absolute;left:430px;top:206px;width:340px;height:52px;display:grid;grid-template-columns:repeat(3,1fr);gap:2px;background:#fff}
.invoice-meta div{background:var(--grey-box);display:flex;flex-direction:column;justify-content:center;padding-left:14px}
.meta-label{font-size:8px;letter-spacing:.5px;color:var(--ink-soft);text-transform:uppercase}
.meta-value{font-size:11.5px;font-weight:700;color:#555}
.meta-value.mono{font-family:"Cutive Mono",monospace;font-weight:400;font-size:10px;letter-spacing:1px}

.items{position:absolute;left:40px;top:300px;width:730px;border-collapse:collapse}
.items th{background:var(--blue);color:#fff;font-family:"Raleway",sans-serif;font-weight:500;font-variant:small-caps;font-size:18px;letter-spacing:3px;height:40px;text-align:left;padding-left:28px}
.items th.num,.items td.num{text-align:center;padding-left:0}
.items td{height:68px;border:2px solid #fff;background:var(--grey-cell);font-size:11px;font-weight:700;color:#666}
.items tr:nth-child(even) td{background:var(--grey-cell-alt)}
.item-cell{padding-left:28px}
.item-name{font-size:13px;font-weight:700;color:#444;display:block;margin-bottom:2px}
.item-note{font-size:8.5px;font-weight:400;color:var(--ink-soft);line-height:1.25;display:block}

.summary{position:absolute;left:560px;top:768px;width:210px}
.summary-lines{background:var(--blue-light);color:#fff;font-size:12px;font-weight:700;padding:12px 18px;line-height:1.55}
.summary-total{background:var(--blue-deep);color:#fff;font-size:13px;font-weight:700;padding:10px 18px;margin-top:2px}
.summary p{display:flex;justify-content:space-between;text-transform:uppercase}

.signoff{position:absolute;left:150px;top:900px;display:flex;align-items:flex-end;gap:14px}
.signoff-word{font-size:15px;color:#444}
.signature{width:300px;height:70px;background:linear-gradient(90deg,#dbe8fb,#eef4fd);border-radius:4px}

.cities{position:absolute;left:0;right:140px;top:1046px;text-align:center;font-family:"Cutive Mono",monospace;font-size:19px;letter-spacing:3px;color:var(--blue-deep)}
.corner{position:absolute;right:0;bottom:0;width:120px;height:160px}
</style>
</head>
<body>
<main class="sheet">
  <header>
    <div class="brand"><span class="brand-dot"></span><span class="brand-name">HARBOURLINE SOURCING</span></div>
    <ul class="contacts">
      <li><svg viewBox="0 0 12 12"><circle cx="6" cy="6" r="6" fill="var(--red)"/><rect x="4" y="2.5" width="4" height="7" rx="1" fill="none" stroke="#fff" stroke-width="1"/></svg>0491 372 618</li>
      <li><svg viewBox="0 0 12 12"><circle cx="6" cy="6" r="6" fill="var(--red)"/><rect x="3" y="4" width="6" height="4.2" fill="none" stroke="#fff" stroke-width="1"/><path d="M3 4l3 2.3L9 4" fill="none" stroke="#fff" stroke-width="1"/></svg>MARCUS@HARBOURLINESOURCING.COM.AU</li>
      <li><svg viewBox="0 0 12 12"><circle cx="6" cy="6" r="6" fill="var(--red)"/><circle cx="6" cy="6" r="3" fill="none" stroke="#fff" stroke-width="1"/><path d="M3 6h6M6 3v6" stroke="#fff" stroke-width=".8"/></svg>HARBOURLINESOURCING.COM.AU</li>
    </ul>
  </header>

  <h1 class="invoice-title">INVOICE</h1>
  <section class="invoice-meta">
    <div><span class="meta-label">Total due</span><span class="meta-value">$15,900.00</span></div>
    <div><span class="meta-label">Invoice date :</span><span class="meta-value">25 JUNE 2015</span></div>
    <div><span class="meta-label">Invoice no :</span><span class="meta-value mono">482000015</span></div>
  </section>

  <table class="items">
    <thead>
      <tr><th style="width:380px">Item Description</th><th class="num">Unit Price</th><th class="num">Quantity</th><th class="num">Total</th></tr>
    </thead>
    <tbody>
      <tr><td class="item-cell"><span class="item-name">Landing Page</span><span class="item-note">Lorem ipsum dolor sit amet, consectetur adipiscing elit, sed do eius-<br>mod tempor incididunt ut labore et dolore magna aliqua.</span></td><td class="num">$2500</td><td class="num">02</td><td class="num">$5000</td></tr>
      <tr><td class="item-cell"><span class="item-name">UI/UX Design</span><span class="item-note">Lorem ipsum dolor sit amet, consectetur adipiscing elit, sed do eius-<br>mod tempor incididunt ut labore et dolore magna aliqua.</span></td><td class="num">$2300</td><td class="num">01</td><td class="num">$2300</td></tr>
      <tr><td class="item-cell"><span class="item-name">Logo Design</span><span class="item-note">Lorem ipsum dolor sit amet, consectetur adipiscing elit, sed do eius-<br>mod tempor incididunt ut labore et dolore magna aliqua.</span></td><td class="num">$1200</td><td class="num">01</td><td class="num">$1200</td></tr>
      <tr><td class="item-cell"><span class="item-name">Graphic Design</span><span class="item-note">Lorem ipsum dolor sit amet, consectetur adipiscing elit, sed do eius-<br>mod tempor incididunt ut labore et dolore magna aliqua.</span></td><td class="num">$1500</td><td class="num">01</td><td class="num">$1500</td></tr>
      <tr><td class="item-cell"><span class="item-name">Wordpress Theme</span><span class="item-note">Lorem ipsum dolor sit amet, consectetur adipiscing elit, sed do eius-<br>mod tempor incididunt ut labore et dolore magna aliqua.</span></td><td class="num">$4000</td><td class="num">01</td><td class="num">$4000</td></tr>
      <tr><td class="item-cell"><span class="item-name">Seo</span><span class="item-note">Lorem ipsum dolor sit amet, consectetur adipiscing elit, sed do eius-<br>mod tempor incididunt ut labore et dolore magna aliqua.</span></td><td class="num">$1900</td><td class="num">01</td><td class="num">$1900</td></tr>
    </tbody>
  </table>

  <section class="summary">
    <div class="summary-lines">
      <p><span>Sub text :</span><span>$ 14000</span></p>
      <p><span>Tax VAT :</span><span>$ 1900</span></p>
    </div>
    <div class="summary-total"><p><span>Tax VAT :</span><span>$ 15900</span></p></div>
  </section>

  <footer>
    <div class="signoff">
      <span class="signoff-word">Sincerely,</span>
      <div class="signature" role="img" aria-label="Handwritten signature in blue ink"></div>
    </div>
    <p class="cities">SYDNEY | MELBOURNE | ADELAIDE | BRISBANE</p>
    <svg class="corner" viewBox="0 0 120 160" aria-hidden="true">
      <polygon points="120,0 120,160 0,160" fill="var(--blue)"/>
      <polygon points="30,160 44,92 70,114 54,160" fill="var(--green)"/>
      <polygon points="120,30 120,72 96,92" fill="var(--orange)"/>
    </svg>
  </footer>
</main>
</body>
</html>
```